A Gentle Crooked Lesson on MOSS plus ways to endure every moment

Not sure.It is about Life injustice and how to face the truth and deal with anything that comes.It touched on Love Identity Finance Emotions

Target Market(s)

18-55

Industry/Entity Type

Life Coaching

Requirements
Must have
• A line through 'Crooked'
Nice to have
• An image that captures the interest

```html
<!DOCTYPE html>
<html lang="en">
<head>
<meta charset="utf-8">
<title>A Gentle Crooked Lesson — Book Cover</title>
<link rel="stylesheet" href="https://fonts.googleapis.com/css2?family=Damion&family=Roboto:wght@300;700;900&display=swap">
<style>
  :root {
    --page-bg: #ffffff;
    --amber-deep: #f2a900;
    --amber-mid: #fbbd12;
    --glow: #fde7a8;
    --glow-core: #fff3d0;
    --ink: #0d0d0d;
  }
  * { margin: 0; padding: 0; box-sizing: border-box; }
  html, body {
    width: 1200px;
    height: 1200px;
    overflow: hidden;
    background: var(--page-bg);
  }
  .cover {
    position: absolute;
    left: 228px;
    top: 50px;
    width: 745px;
    height: 1100px;
    overflow: hidden;
    background:
      radial-gradient(ellipse 60% 48% at 50% 52%, var(--glow-core) 0%, var(--glow) 30%, var(--amber-mid) 70%, var(--amber-deep) 100%);
    color: var(--ink);
    font-family: "Roboto", Arial, sans-serif;
    text-align: center;
  }
  .title-lead {
    position: absolute;
    left: 0; right: 0;
    top: 100px;
    font-family: "Damion", cursive;
    font-size: 118px;
    line-height: 1;
    transform: rotate(-2deg);
  }
  .title-struck {
    position: absolute;
    left: 0; right: 0;
    top: 222px;
    font-weight: 900;
    font-size: 132px;
    line-height: 1;
    letter-spacing: -1px;
  }
  .strike-line {
    position: absolute;
    left: 78px;
    top: 296px;
    width: 600px;
    height: 3px;
    background: var(--ink);
  }
  .title-main {
    position: absolute;
    left: 0; right: 0;
    top: 400px;
    font-weight: 700;
    font-size: 150px;
    line-height: 1;
    letter-spacing: -2px;
  }
  .subtitle {
    position: absolute;
    left: 0; right: 0;
    top: 566px;
    font-weight: 300;
    font-size: 46px;
    line-height: 1.15;
  }
  .scene-art {
    position: absolute;
    left: 0;
    top: 690px;
    width: 745px;
    height: 410px;
    background: linear-gradient(180deg, rgba(242,169,0,0) 0%, rgba(242,169,0,0.35) 55%, rgba(20,14,0,0.85) 100%);
  }
  .author {
    position: absolute;
    left: 0; right: 0;
    top: 948px;
    font-weight: 700;
    font-size: 44px;
    line-height: 1.2;
    letter-spacing: 0.5px;
    color: var(--ink);
  }
</style>
</head>
<body>
  <main class="cover">
    <div class="title-lead">A Gentle</div>
    <div class="title-struck">CROOKED</div>
    <div class="strike-line"></div>
    <div class="title-main">LESSON</div>
    <p class="subtitle">on MOSS plus ways<br>to endure every moment</p>
    <div class="scene-art" role="img" aria-label="Silhouette of a person leaping across a gap between two dark cliff edges"></div>
    <p class="author">TEO R<br>VARNHOLM</p>
  </main>
</body>
</html>
```